Unique Elegant Stationary Set

Prepare a unique eye catching stationary set consisting of :
(1) Letterhead
(2) A3 Envelope
(3) Business Card
(4) Email Signature Banner

Package to be elegant, modern, and designers not only to think of design or colors but also materials could make a big difference, embossing, debossing, glossy, matt ....etc.

I attached both our new logos (Stacked or Linear) noting you may use any of them but you cant modify anything in the logos. Also attached our final draft portfolio to see what type of projects we work on and i also have here a glimmerboard page link showing the direction we want: https://www.glimmerboard.example/dorvanmelik/business-card-design/

Target Market(s)

VVIP / Elite Developers

Industry/Entity Type

Architecture

Font styles to use
Sans Serif
Other font styles liked:
• unitext

Requirements
Should not have
• too many colors, or being busy in general. We want something pleasing to the eye

```html
<!DOCTYPE html>
<html lang="en">
<head>
<meta charset="utf-8">
<title>Kelvo Studio — Stationery Set</title>
<link rel="stylesheet" href="https://fonts.googleapis.com/css2?family=Arimo:wght@400;700&family=Poppins:wght@300;400;500;600;700&family=Roboto+Condensed:wght@300;400;700&display=swap">
<style>
  :root {
    --bg: #d5dbde;
    --paper: #ffffff;
    --ink: #4a4a4c;
    --ink-dark: #2b2b2d;
    --red: #c8202a;
    --band: #5d5d60;
    --card: #262628;
    --card-deep: #1d1d1f;
    --muted: #e9e9ea;
  }
  * { box-sizing: border-box; margin: 0; padding: 0; }
  html, body { width: 1200px; height: 698px; overflow: hidden; }
  body { background: var(--bg); position: relative; font-family: "Poppins", sans-serif; color: var(--ink); }
  .piece { position: absolute; box-shadow: 0 4px 12px rgba(0,0,0,.22); }

  /* wordmark */
  .wordmark { position: absolute; color: var(--red); font-family: "Poppins", sans-serif; font-weight: 700; letter-spacing: .04em; white-space: nowrap; display: flex; align-items: center; gap: .3em; line-height: 1; }
  .wordmark .dot { width: .32em; height: .32em; background: var(--red); display: inline-block; }

  .band { position: absolute; left: 0; bottom: 0; width: 100%; display: block; }
  .icon { width: 1em; height: 1em; fill: var(--red); flex: none; }
  .contact-row { display: flex; align-items: center; gap: .45em; white-space: nowrap; }

  /* letterhead */
  .letterhead { left: 73px; top: 60px; width: 425px; height: 599px; background: var(--paper); }
  .letterhead .wordmark { font-size: 17px; left: 0; right: 0; top: 20px; justify-content: center; }
  .letterhead .rule { position: absolute; left: 0; right: 0; height: 1.5px; background: var(--band); }
  .letterhead .sender { position: absolute; left: 23px; top: 105px; }
  .person-name { font-family: "Roboto Condensed", sans-serif; font-size: 20px; color: var(--ink); line-height: 1; }
  .person-name b { font-weight: 700; }
  .person-name span { font-weight: 300; }
  .person-role { font-family: "Arimo", sans-serif; font-weight: 700; font-size: 8.5px; color: var(--ink); margin-top: 2px; margin-left: 1px; }
  .sender-contacts { margin-top: 10px; font-family: "Arimo", sans-serif; font-size: 8px; line-height: 10px; }
  .sender-contacts .icon { fill: var(--ink); }
  .letter-date { position: absolute; right: 23px; top: 114px; font-family: "Arimo", sans-serif; font-weight: 700; font-size: 10px; color: var(--ink); }
  .letter-body { position: absolute; left: 23px; width: 379px; top: 198px; font-family: "Arimo", sans-serif; font-size: 9.2px; line-height: 12.2px; text-align: justify; color: var(--ink); }
  .letter-body p + p { margin-top: 12px; }
  .signature { position: absolute; left: 23px; top: 409px; width: 145px; height: 45px; background: linear-gradient(90deg, #f1f1f2, #e6e6e8); }
  .signer { position: absolute; left: 23px; top: 457px; }
  .signer .person-name { font-size: 19px; }
  .letter-footer { position: absolute; left: 0; right: 0; top: 545px; font-size: 9px; color: var(--ink-dark); }
  .letter-footer .addr { justify-content: center; }
  .letter-footer .line { display: flex; justify-content: space-between; padding: 0 30px 0 26px; margin-top: 9px; }

  /* envelope */
  .envelope-back { left: 519px; top: 62px; width: 346px; height: 153px; background: var(--paper); }
  .envelope-back .wordmark { font-size: 15px; right: 8px; top: 20px; }
  .envelope-back .rule { position: absolute; left: 0; right: 0; top: 116px; height: 1px; background: var(--band); }
  .envelope-back .addr { position: absolute; left: 0; right: 0; top: 122px; justify-content: center; font-size: 6.6px; color: var(--ink-dark); }
  .envelope-back .line { position: absolute; left: 38px; right: 38px; top: 133px; display: flex; justify-content: space-between; font-size: 6.6px; color: var(--ink-dark); }
  .envelope-front { left: 521px; top: 232px; width: 344px; height: 153px; background: var(--paper); }
  .envelope-front .flap { position: absolute; left: 3px; right: 3px; top: 0; height: 52px; background: var(--paper); border-radius: 0 0 14px 14px; box-shadow: 0 6px 10px rgba(0,0,0,.14); }
  .envelope-front .wordmark { font-size: 10px; left: 0; right: 0; top: 20px; justify-content: center; }

  /* cards */
  .card-back { left: 881px; top: 63px; width: 269px; height: 154px; background: linear-gradient(135deg, var(--card-deep), #2e2e30); }
  .card-front { left: 881px; top: 232px; width: 269px; height: 153px; background: var(--card); color: #fff; }
  .card-front .wordmark { font-size: 12.5px; left: 9px; top: 75px; }
  .vrule { position: absolute; width: 1px; background: var(--red); }
  .card-front .vrule { left: 134px; top: 29px; height: 94px; }
  .card-info { position: absolute; left: 158px; top: 31px; font-size: 6.9px; line-height: 9.8px; }
  .card-info .name { font-size: 14.5px; line-height: 1; }
  .name b { color: var(--red); font-weight: 500; }
  .name span { color: var(--muted); font-weight: 300; }
  .card-info .title { font-weight: 500; margin-top: 1px; }
  .card-info .addr { margin-top: 6px; }
  .card-info .contacts { margin-top: 5px; }

  /* email banner */
  .email-banner { left: 537px; top: 432px; width: 592px; height: 198px; background: var(--card); color: #fff; }
  .email-banner .pattern { position: absolute; inset: 0; background: linear-gradient(135deg, var(--card-deep), #303032); }
  .email-banner .wordmark { font-size: 27px; left: 30px; top: 80px; }
  .email-banner .vrule { left: 295px; top: 25px; height: 133px; }
  .email-banner .card-info { left: 347px; top: 25px; font-size: 12.5px; line-height: 15.6px; }
  .email-banner .card-info .name { font-size: 28px; }
  .email-banner .card-info .title { margin-top: 2px; }
  .email-banner .card-info .addr { margin-top: 10px; }
  .email-banner .card-info .contacts { margin-top: 10px; }
</style>
</head>
<body>

<svg width="0" height="0" style="position:absolute" aria-hidden="true">
  <symbol id="i-pin" viewBox="0 0 16 16"><path d="M8 1a5 5 0 0 0-5 5c0 3.8 5 9 5 9s5-5.2 5-9a5 5 0 0 0-5-5zm0 7a2 2 0 1 1 0-4 2 2 0 0 1 0 4z"/></symbol>
  <symbol id="i-phone" viewBox="0 0 16 16"><path d="M4 1.5l2.2 2.6-1.3 1.7a9 9 0 0 0 5.3 5.3l1.7-1.3L14.5 12l-1.6 2.2C7.6 14.4 1.6 8.4 1.8 3.1z"/></symbol>
  <symbol id="i-globe" viewBox="0 0 16 16"><path d="M8 1a7 7 0 1 0 0 14A7 7 0 0 0 8 1zm0 1.4c.9.8 1.6 2.2 1.9 3.9H6.1C6.4 4.6 7.1 3.2 8 2.4zM2.5 7.5h2.2c0 .4 0 .7.1 1.1H2.5a5.6 5.6 0 0 1 0-1.1zm3.6 2.4h3.8c-.3 1.7-1 3-1.9 3.8-.9-.8-1.6-2.1-1.9-3.8zm5.2-1.3c.1-.4.1-.7.1-1.1h2.2a5.6 5.6 0 0 1 0 1.1z"/></symbol>
  <symbol id="i-mail" viewBox="0 0 16 16"><path d="M1.5 6L8 1.8 14.5 6v8h-13zm1.6.9L8 10.2l4.9-3.3L8 3.6zM3 8.4V12.6h10V8.4L8 11.8z"/></symbol>
</svg>

<!-- Letterhead -->
<section class="piece letterhead">
  <div class="wordmark">KELVO STUDIO<i class="dot"></i></div>
  <div class="rule" style="top:50px"></div>

  <div class="sender">
    <div class="person-name"><b>Mirela</b> <span>Vostal</span></div>
    <div class="person-role">Founder &amp; CEO</div>
    <div class="sender-contacts">
      <div class="contact-row"><svg class="icon"><use href="#i-phone"/></svg>(555) 019-7477</div>
      <div class="contact-row"><svg class="icon"><use href="#i-globe"/></svg>www.kelvo.example</div>
      <div class="contact-row"><svg class="icon"><use href="#i-mail"/></svg>info@kelvo.example</div>
    </div>
  </div>
  <div class="letter-date">August-05-2019</div>

  <div class="letter-body">
    <p>Lorem ipsum dolor sit amet, consectetuer adipiscing elit, sed diam nonummy nibh euismod tincidunt ut laoreet dolore magna aliquam erat volutpat. Ut wisi enim ad minim veniam, quis nostrud exerci tation ullamcorper suscipit lobortis</p>
    <p>Lorem ipsum dolor sit amet, cons ectetuer adipiscing elit, sed diam nonummy nibh euismod tincidunt ut laoreet dolore magna aliquam erat volutpat. Ut wisi enim ad minim veniam, quis nostrud exerci tation ullamcorper suscipit lobortis nisl ut aliquip ex ea commodo consequat. Lorem ipsum dolor sit amet, consectetuer olutpat. Ut wisi enim ad minim veniam, quis nostrud exerci tation ullamcorper suscipit lobortis nisl ut aliquip ex ea commodo consequat. Duis autem</p>
    <p>vel eum iriure dolor in hendrerit in vulputate velit esse molestie consequat, vel illum dolore eu feugiat nulla facilisis at vero eros et accumsan et iusto odio dignissim qui blandit praesent luptatum zzril delenit augue duis dolore te feugait nulla facilisi. Lorem ipsum dolor sit amet, cons ectetuer adipiscing elit, sed diam nonummy nibh euismod tincidunt ut laoreet dolore magna aliquam erat volutpat. Ut wisi enim .</p>
  </div>

  <div class="signature" role="img" aria-label="Handwritten signature of the director"></div>
  <div class="signer">
    <div class="person-name"><b>Tamsin</b> <span>Korvel</span></div>
    <div class="person-role">Director</div>
  </div>

  <div class="rule" style="top:537px"></div>
  <div class="letter-footer">
    <div class="contact-row addr"><svg class="icon"><use href="#i-pin"/></svg>418 Larchmont Ave. Suite 310, Brookvale, TX 75990</div>
    <div class="line">
      <div class="contact-row"><svg class="icon"><use href="#i-phone"/></svg>(555) 014-2738</div>
      <div class="contact-row"><svg class="icon"><use href="#i-mail"/></svg>info@kelvo.example</div>
      <div class="contact-row"><svg class="icon"><use href="#i-globe"/></svg>www.kelvo.example</div>
    </div>
  </div>
  <svg class="band" width="425" height="13" viewBox="0 0 425 13" aria-hidden="true">
    <rect width="425" height="13" fill="var(--band)"/>
    <polygon points="184,13 197,0 239,0 226,13" fill="#fff"/>
    <polygon points="190,13 203,0 212,0 199,13" fill="var(--red)"/>
    <polygon points="204,13 217,0 226,0 213,13" fill="var(--red)"/>
  </svg>
</section>

<!-- Envelope, address side -->
<section class="piece envelope-back">
  <div class="wordmark">KELVO STUDIO<i class="dot"></i></div>
  <div class="rule"></div>
  <div class="contact-row addr"><svg class="icon"><use href="#i-pin"/></svg>72 Millbrook Lane, Ashcombe, Kent, ME9 4QT</div>
  <div class="line">
    <div class="contact-row"><svg class="icon"><use href="#i-phone"/></svg>(555) 014-2738</div>
    <div class="contact-row"><svg class="icon"><use href="#i-mail"/></svg>info@kelvo.example</div>
    <div class="contact-row"><svg class="icon"><use href="#i-globe"/></svg>www.kelvo.example</div>
  </div>
  <svg class="band" width="346" height="6" viewBox="0 0 346 6" aria-hidden="true">
    <rect width="346" height="6" fill="var(--band)"/>
    <polygon points="157,6 163,0 191,0 185,6" fill="#fff"/>
    <polygon points="162,6 168,0 175,0 169,6" fill="var(--red)"/>
    <polygon points="173,6 179,0 186,0 180,6" fill="var(--red)"/>
  </svg>
</section>

<!-- Envelope, flap side -->
<section class="piece envelope-front">
  <div class="flap"></div>
  <div class="wordmark">KELVO STUDIO</div>
</section>

<!-- Business card, back -->
<section class="piece card-back" role="img" aria-label="Dark embossed repeat of the studio name across the card back"></section>

<!-- Business card, front -->
<section class="piece card-front">
  <div class="wordmark">KELVO STUDIO<i class="dot"></i></div>
  <div class="vrule"></div>
  <div class="card-info">
    <div class="name"><b>Mirela</b> <span>Vostal</span></div>
    <div class="title">Founder &amp; CEO</div>
    <div class="addr">418 Larchmont Ave. Suite<br>310 Brookvale, TX 75990</div>
    <div class="contacts">
      <div class="contact-row"><svg class="icon"><use href="#i-phone"/></svg>(555) 014-2738</div>
      <div class="contact-row"><svg class="icon"><use href="#i-globe"/></svg>info@kelvo.example</div>
      <div class="contact-row"><svg class="icon"><use href="#i-mail"/></svg>www.kelvo.example</div>
    </div>
  </div>
  <svg class="band" width="269" height="9" viewBox="0 0 269 9" aria-hidden="true">
    <rect width="269" height="9" fill="var(--band)"/>
    <polygon points="114,9 123,0 152,0 143,9" fill="var(--card)"/>
    <polygon points="119,9 128,0 135,0 126,9" fill="var(--red)"/>
    <polygon points="131,9 140,0 147,0 138,9" fill="var(--red)"/>
  </svg>
</section>

<!-- Email signature banner -->
<section class="piece email-banner">
  <div class="pattern" role="img" aria-label="Dark embossed repeat of the studio name as background texture"></div>
  <div class="wordmark">KELVO STUDIO<i class="dot"></i></div>
  <div class="vrule"></div>
  <div class="card-info">
    <div class="name"><b>Mirela</b> <span>Vostal</span></div>
    <div class="title">Founder &amp; CEO</div>
    <div class="addr">418 Larchmont Ave. Suite 310<br>Brookvale, TX 75990</div>
    <div class="contacts">
      <div class="contact-row"><svg class="icon"><use href="#i-phone"/></svg>(555) 014-2738</div>
      <div class="contact-row"><svg class="icon"><use href="#i-globe"/></svg>info@kelvo.example</div>
      <div class="contact-row"><svg class="icon"><use href="#i-mail"/></svg>www.kelvo.example</div>
    </div>
  </div>
  <svg class="band" width="592" height="15" viewBox="0 0 592 15" aria-hidden="true">
    <rect width="592" height="15" fill="var(--band)"/>
    <polygon points="265,15 280,0 326,0 311,15" fill="var(--card-deep)"/>
    <polygon points="272,15 287,0 298,0 283,15" fill="var(--red)"/>
    <polygon points="291,15 306,0 317,0 302,15" fill="var(--red)"/>
  </svg>
</section>

</body>
</html>
```